Business Card Design for Pastor/Church Leadership - simple, elegant, "different"

Design a name card based on logo and color from our branding guide - see file "MBF Logo and Color".
The teal frame around the logo is not part of the logo and is a not necessary design element for the name card (as the attached PDF file may suggest).
The font suggested by branding is "Frutiger 55 Roman".
The file "not good.pdf", a sample of a name card that is NOT good.
- fonts too small to read
- the tagline on the logo "Still waters, open door" not easy to read with logo used in this design
- "MAPLE GROVE FELLOWSHIP" unnecessarily duplicated - possibly because logo too small
- not sure about the green frame, probably better to drop

Target Market(s)

broad, all people the pastor of an international church in Tokyo meets

Industry/Entity Type

Business

Contact Information for Business Card

Mattias R. Pellworth
Pastor
3-9-4 Kawaranodai, Kaedeno-ku
Tokyo 162-0847 (Church)
2-21 Ochibamachi, Kaedeno-ku
Tokyo 162-0853 (Home)
Tel: 03-5817-2963
E-mail: pastor@maplegrovefell.org
URL: http://www.maplegrovefell.org

Font styles to use
Sans Serif
Other font styles liked:
• Frutiger 55 Roman (want, not must)

Requirements
Must have
• must include logo
• must make use of the "bright turquoise color"
• Cyan = 59, Magenta = 0, Yellow=24, Black=0
• Red=3.1%, Green=91%, Blue=87.1%
• Key Info (name) must be easy to read (see notes on bad sample namecard attached)

```html
<!DOCTYPE html>
<html lang="en">
<head>
<meta charset="utf-8">
<title>Maple Grove Fellowship – Pastor Business Card</title>
<link rel="stylesheet" href="https://fonts.googleapis.com/css2?family=Open+Sans:wght@400;600&display=swap">
<style>
  :root {
    --canvas: #e9e6e1;
    --card-dark: #232425;
    --card-dark-edge: #1a1b1c;
    --band: #ecedec;
    --teal: #5fc7cb;
    --text-light: #f2f2f2;
    --font-body: "Open Sans", "Helvetica Neue", Arial, sans-serif;
  }
  * { box-sizing: border-box; margin: 0; padding: 0; }
  html, body {
    width: 1200px; height: 1022px; overflow: hidden;
    background: var(--canvas);
    font-family: var(--font-body);
  }
  .canvas { position: relative; width: 1200px; height: 1022px; }

  .card {
    position: absolute; left: 180px;
    width: 840px; height: 480px;
    background: linear-gradient(135deg, var(--card-dark) 0%, var(--card-dark-edge) 100%);
    overflow: hidden;
    box-shadow: 0 6px 18px rgba(0,0,0,.18);
  }
  .card--front { top: 22px; }
  .card--back  { top: 520px; }

  .card__band {
    position: absolute; top: 0; bottom: 0; width: 48px;
    background: var(--band);
  }
  .card__band--left  { left: 0; }
  .card__band--right { right: 0; }

  /* Front: wordmark */
  .wordmark {
    position: absolute; display: flex; align-items: center; gap: 14px;
    color: var(--teal); font-weight: 600; letter-spacing: 4px;
    white-space: nowrap;
  }
  .card--front .wordmark { top: 56px; right: 96px; font-size: 64px; }
  .wordmark__square {
    display: block; width: 22px; height: 22px; background: var(--teal);
  }

  /* Front: contact block */
  .contact {
    position: absolute; left: 84px; bottom: 40px;
    color: var(--text-light); font-size: 16px; line-height: 1.32;
  }
  .contact__org {
    color: var(--teal); font-size: 18px; letter-spacing: 2px;
    text-transform: uppercase; padding-bottom: 6px;
    border-bottom: 2px solid var(--teal); display: inline-block;
    padding-right: 40px;
  }
  .contact__tagline { color: var(--teal); font-size: 17px; margin: 6px 0 12px 34px; }
  .contact__person { margin-left: 34px; }
  .contact__name { color: var(--teal); font-size: 28px; line-height: 1.15; }
  .contact__title { font-size: 16px; margin-bottom: 12px; }
  .contact__address { margin-left: 34px; margin-bottom: 10px; }
  .contact__note { color: var(--teal); }
  .contact__lines { margin-left: 34px; list-style: none; }
  .contact__label { color: var(--teal); display: inline-block; width: 24px; }

  /* Back */
  .card--back .wordmark { left: 0; right: 0; top: 0; bottom: 0; justify-content: center; font-size: 120px; gap: 26px; }
  .card--back .wordmark__square { width: 40px; height: 40px; }
</style>
</head>
<body>
<main class="canvas">

  <section class="card card--front" aria-label="Business card, front">
    <div class="card__band card__band--left"></div>
    <div class="card__band card__band--right"></div>

    <div class="wordmark"><span class="wordmark__square"></span>MBF</div>

    <div class="contact">
      <p class="contact__org">Maple Grove Fellowship</p>
      <p class="contact__tagline">Still waters, open door</p>
      <div class="contact__person">
        <p class="contact__name">Mattias R. Pellworth</p>
        <p class="contact__title">Pastor</p>
      </div>
      <p class="contact__address">3-9-4 Kawaranodai, Kaedeno-ku<br>Tokyo 162-0847 <span class="contact__note">(Church)</span></p>
      <p class="contact__address">2-21 Ochibamachi, Kaedeno-ku<br>Tokyo 162-0853 <span class="contact__note">(Home)</span></p>
      <ul class="contact__lines">
        <li><span class="contact__label">T:</span>03-5817-2963</li>
        <li><span class="contact__label">E:</span>pastor@maplegrovefell.org</li>
        <li><span class="contact__label">W:</span>www.maplegrovefell.org</li>
      </ul>
    </div>
  </section>

  <section class="card card--back" aria-label="Business card, back">
    <div class="card__band card__band--left"></div>
    <div class="card__band card__band--right"></div>
    <div class="wordmark"><span class="wordmark__square"></span>MBF</div>
  </section>

</main>
</body>
</html>
```